WILLOWMERE PERK WEBSITE HOME PAGE AND CHECKOUT PAGES

UPDATE TO BRIEF:

Willowmere Perks is a company that provides Charities with the Free Vacation Vouchers that they can use to incentivize people to donate which in turn increases donations for the chairty.

So I need to keep it a little more template like the example url I gave. http://plinthframes.com/willowmere-perk/ Because, I am going to provide template to ANY CHARITY TYPE and they just fill in the content into the template and change images or whatever for their charity. So I am really looking for a website template that can be used for multiple and different kinds of charities.

So where the logo would go please use YOUR LOGO HERE generic logo for now

and where ever you promote the Free Vacation Certificate To Las Vegas please add "Brought To You By" (logo willowmere perks or something...basically its a partnership with the Charity and Willowmere Perk)

So Willowmere Perk is a marketing company and not a Charity but more of a plug and play platform that allows a charity to accepts donations and immediately deliver the promised incentive offer after donation is made on the website.

When a Charity is able to offer a high perceived value gift for a donation they increase donations.

Target Market(s)

PEOPLE THAT DONATE TO CHARITIES

Industry/Entity Type

Charity

Number of Pages Required

3 page

Requirements
Must have
• One thing i need to add to the website is an Incentive Gift for the Donation.

So I need this tagline and images to make the promotion seem great:
"Donate $100 and Receive A Free 3 Night Vacation Certificate To Las Vegas!"

Maybe show image of vegas or some kind of nice graphic that promotes the vegas vacation as a gift for the $100 donation very well"

I need the payment pages as well. So when someone click Donate Now, the next page is there where they can see their gift that is included with the donation, and also the donation amount...
Nice to have

Should not have

```html
<!DOCTYPE html>
<html lang="en">
<head>
<meta charset="utf-8">
<title>Willowmere Perk – Checkout Page</title>
<link rel="stylesheet" href="https://fonts.googleapis.com/css2?family=Open+Sans:wght@300;400;600;700;800&display=swap">
<style>
  :root {
    --board: #5a5b5d;
    --ink: #111111;
    --white: #ffffff;
    --mint: #00e69c;
    --field: #efefef;
    --placeholder: #b9b9b9;
    --outline: #9a9a9a;
    --gold: #e0b21a;
    --orange: #e8950f;
    --red: #d3201c;
    --teal: #0e6f7e;
    --shade: rgba(0, 0, 0, 0.62);
  }
  * { box-sizing: border-box; margin: 0; padding: 0; }
  html, body { width: 1200px; height: 843px; overflow: hidden; }
  body {
    position: relative;
    background: var(--board);
    font-family: "Open Sans", sans-serif;
    color: var(--ink);
  }
  .board-title {
    position: absolute; top: 62px; left: 0; width: 1200px;
    text-align: center; color: var(--white);
    font-size: 26px; font-weight: 300; letter-spacing: 0.2px;
  }
  .page {
    position: absolute; left: 41px; top: 168px; width: 1118px; height: 628px;
    overflow: hidden;
  }
  .page-rule {
    position: absolute; left: 41px; top: 806px; width: 1118px; height: 2px;
    background: var(--white);
  }
  .hero {
    position: absolute; left: 0; top: 0; width: 1118px; height: 495px;
    background: linear-gradient(100deg, #6f87a8 0%, #c7b39a 30%, #b98d6a 55%, #e2c3a9 75%, #8fa7bd 100%);
  }
  .hero-base {
    position: absolute; left: 0; top: 492px; width: 1118px; height: 3px; background: #9bc23a;
  }
  .logo-badge {
    position: absolute; left: 162px; top: 21px; width: 44px; height: 44px; border-radius: 50%;
    background: #8a8a8a; color: #333; font-size: 8px; font-weight: 600;
    display: flex; align-items: center; justify-content: center;
  }
  .btn-gold {
    position: absolute; background: var(--gold); color: #111;
    font-weight: 700; letter-spacing: 1px;
    display: flex; align-items: center; justify-content: center;
  }
  .nav-donate { left: 851px; top: 28px; width: 106px; height: 31px; font-size: 9px; }
  .promo {
    position: absolute; left: 162px; top: 149px; width: 460px; height: 307px;
    background: rgba(20, 30, 40, 0.75); border-radius: 8px; overflow: hidden;
  }
  .promo-headline {
    position: absolute; left: 26px; top: 14px;
    font-size: 46px; font-weight: 800; color: var(--orange); letter-spacing: -1.5px;
  }
  .promo-tag {
    position: absolute; left: 196px; top: 6px; width: 120px; height: 72px;
    background: var(--white); border-radius: 8px;
    font-size: 38px; font-weight: 800; color: var(--red); padding-left: 12px; line-height: 72px;
  }
  .promo-line {
    position: absolute; left: 26px; color: #e8e8e8; font-weight: 700; white-space: nowrap;
  }
  .promo-line .small { font-size: 19px; }
  .promo-line .big { font-size: 28px; }
  .promo-line .gold { color: var(--gold); font-size: 28px; font-weight: 800; }
  .promo-donate { left: 26px; top: 180px; width: 131px; height: 38px; font-size: 12px; }
  .promo-foot {
    position: absolute; left: 0; top: 243px; width: 460px; height: 64px; background: #d9d9d9;
  }
  .promo-foot .by {
    position: absolute; left: 82px; top: 22px; font-size: 12px; color: #333;
  }
  .promo-foot .partner {
    position: absolute; left: 190px; top: 21px; font-size: 13px; font-weight: 700; color: #1d6fa8;
  }
  .photo-family {
    position: absolute; left: 740px; top: 150px; width: 370px; height: 345px;
    background: radial-gradient(ellipse at 55% 45%, #e9bfa3 0%, #c98e70 45%, rgba(200,140,110,0) 75%);
  }
  .band {
    position: absolute; left: 0; top: 495px; width: 1118px; height: 133px; background: var(--teal);
  }
  .band-title {
    position: absolute; left: 266px; top: 15px; font-size: 15px; font-weight: 700; color: #9fd2d9;
  }
  .amount {
    position: absolute; top: 49px; width: 92px; height: 39px;
    display: flex; align-items: center; justify-content: center;
    font-size: 14px; font-weight: 700; color: var(--white);
  }
  .amount.active { background: var(--orange); left: 266px; }
  .amount.plain { background: #3f8f9b; }
  .amount.other { border: 1px solid #9fd2d9; background: transparent; font-weight: 400; }
  .band-donate { left: 704px; top: 49px; width: 132px; height: 39px; font-size: 12px; }
  .band-check {
    position: absolute; left: 266px; top: 92px; font-size: 10px; color: #cfe7ea;
    display: flex; align-items: center; gap: 8px;
  }
  .band-check .box { width: 12px; height: 12px; background: #cfe7ea; }
  .shade { position: absolute; inset: 0; background: var(--shade); }

  .donation-modal {
    position: absolute; left: 446px; top: 221px; width: 340px; height: 512px;
    background: var(--white); border-radius: 4px;
  }
  .modal-title {
    position: absolute; top: 26px; width: 100%; text-align: center;
    font-size: 21px; font-weight: 700; letter-spacing: 0.5px;
  }
  .modal-gift {
    position: absolute; top: 62px; width: 100%; text-align: center;
    font-size: 20px; font-weight: 700; line-height: 28px;
  }
  .field {
    position: absolute; left: 45px; width: 250px; height: 37px; border-radius: 3px;
    background: var(--field); display: flex; align-items: center; padding: 0 14px;
    font-size: 14px;
  }
  .field.amount-field { top: 140px; justify-content: space-between; font-weight: 700; padding: 0 14px 0 16px; }
  .field.placeholder { color: var(--placeholder); padding-left: 12px; }
  .field.name { top: 242px; }
  .field.email { top: 285px; }
  .freq {
    position: absolute; top: 189px; width: 119px; height: 38px; border-radius: 3px;
    background: var(--mint); display: flex; align-items: center; justify-content: center;
    font-size: 13px; font-weight: 700; letter-spacing: 0.5px;
  }
  .freq.once { left: 45px; }
  .freq.monthly { left: 176px; }
  .pay-option {
    position: absolute; left: 45px; width: 250px; height: 38px; border: 1px solid var(--outline);
    border-radius: 3px; display: flex; align-items: center; padding: 0 12px 0 16px; font-size: 14px;
  }
  .pay-option.card { top: 338px; }
  .pay-option.wallet { top: 385px; padding-left: 14px; }
  .pay-option .label { flex: 1; margin-left: 12px; }
  .pay-option .wallet-name { flex: 1; font-weight: 700; color: var(--ink); font-size: 14px; }
  .radio { width: 16px; height: 16px; border: 1px solid #555; border-radius: 50%; }
  .proceed {
    position: absolute; left: 45px; top: 444px; width: 250px; height: 44px; border-radius: 3px;
    background: var(--mint); color: var(--white); font-size: 13px; font-weight: 700;
    letter-spacing: 0.6px; display: flex; align-items: center; padding-left: 23px;
  }
</style>
</head>
<body>
  <h1 class="board-title">CHECKOUT PAGE</h1>

  <main class="page">
    <div class="hero" role="img" aria-label="Las Vegas skyline photo with a smiling family on the right"></div>
    <div class="photo-family" role="img" aria-label="Photo of a family embracing"></div>
    <div class="hero-base"></div>

    <div class="logo-badge">LOGO</div>
    <div class="btn-gold nav-donate">DONATE NOW</div>

    <section class="promo">
      <div class="promo-headline">Donate</div>
      <div class="promo-tag">$1</div>
      <div class="promo-line" style="top:88px;"><span class="small">Receive A </span><span class="big">Free 3 N</span></div>
      <div class="promo-line" style="top:126px;"><span class="small">Certificate To </span><span class="gold">LAS VE</span></div>
      <div class="btn-gold promo-donate">DONATE NOW</div>
      <div class="promo-foot">
        <span class="by">Brought To You By</span>
        <span class="partner">Willowmere Perks</span>
      </div>
    </section>

    <section class="band">
      <div class="band-title">Receive A Free 3 Night Vacation</div>
      <div class="amount active">$100</div>
      <div class="amount plain" style="left:376px;">$200</div>
      <div class="amount plain" style="left:485px;">$350</div>
      <div class="amount other" style="left:595px;">Other</div>
      <div class="btn-gold band-donate">DONATE NOW</div>
      <div class="band-check"><span class="box"></span>I will like to make this Donation Monthly</div>
    </section>

    <div class="shade"></div>
  </main>
  <div class="page-rule"></div>

  <section class="donation-modal">
    <h2 class="modal-title">DONATION</h2>
    <p class="modal-gift">For Free 3 Night Vacation<br>Certificate To Las Vegas!</p>
    <div class="field amount-field"><span>$100</span><span>USD</span></div>
    <div class="freq once">ONCE</div>
    <div class="freq monthly">MONTHLY</div>
    <div class="field placeholder name">NAME</div>
    <div class="field placeholder email">EMAIL</div>
    <div class="pay-option card">
      <svg width="22" height="18" viewBox="0 0 22 18" aria-hidden="true">
        <rect x="1" y="1" width="20" height="16" rx="2" fill="none" stroke="#111" stroke-width="2"/>
        <rect x="1" y="5" width="20" height="3" fill="#111"/>
      </svg>
      <span class="label">Credit Card</span>
      <span class="radio"></span>
    </div>
    <div class="pay-option wallet">
      <span class="wallet-name">Quillpurse</span>
      <span class="radio"></span>
    </div>
    <div class="proceed">PROCEED TO DONATE $100</div>
  </section>
</body>
</html>
```